LearnWave Progress Alliance Business Card

Create a very cool business card. Logo is attached.

Learnwave Progress Alliance Mission

The purposes for which the corporation is organized are to promote social welfare within the meaning of section 501(c)(4) of the Internal Revenue Code, including but not limited to: (1) developing and advocating for legislation, regulations, and government programs that improve education through the use of technology, online enabled course design, personalize instruction and increased student engagement; (2) promoting digital literacy driven by private, public and philanthropic efforts that utilize technology for student learning; (3) advocate for competency based educational efforts built upon digital tools, devices and content that support learning programs; (4) develop policy positions that ensure that poor, minority status, and disadvantaged students will benefit from innovative technologies which should provide increased instructional opportunities for postsecondary success and career advancement; (5) conducting research and publicizing positions of higher education institutions and elected officials concerning these issues

Info for Card:

Mark Halvorsen, Founder
LearnWave Progress Alliance
412 West Marlow Ave, 6th Floor
Pasadena, CA 91187
o (626) 555-0172
f (626) 555-0189
mark@learnwaveprogress.org
website: learnwaveprogress.org

```html
<!DOCTYPE html>
<html lang="en">
<head>
<meta charset="utf-8">
<title>LearnWave Progress Alliance – Business Card</title>
<link href="https://fonts.googleapis.com/css2?family=Arimo:wght@400;700&display=swap" rel="stylesheet">
<style>
  :root {
    --brand-blue: #2f4fa3;
    --card-surface: #e8ebe9;
    --card-edge: #d3d8d5;
    --page-bg: #f3f4f3;
  }
  * { margin: 0; padding: 0; box-sizing: border-box; }
  html, body {
    width: 1200px;
    height: 902px;
    overflow: hidden;
    background: var(--page-bg);
    font-family: "Arimo", Arial, sans-serif;
  }
  .canvas {
    position: relative;
    width: 1200px;
    height: 902px;
  }
  .business-card {
    position: absolute;
    left: 100px;
    top: 165px;
    width: 1000px;
    height: 572px;
    background: var(--card-surface);
    border: 1px solid var(--card-edge);
    border-radius: 30px;
    overflow: hidden;
    color: var(--brand-blue);
  }
  .accent-arc {
    position: absolute;
    inset: 0;
    width: 1000px;
    height: 572px;
  }
  .brand-lockup {
    position: absolute;
    left: 74px;
    top: 110px;
    width: 320px;
    display: flex;
    flex-direction: column;
    align-items: center;
    text-align: center;
  }
  .brand-mark {
    width: 130px;
    height: 130px;
    border-radius: 50%;
    background: var(--brand-blue);
    margin-bottom: 26px;
  }
  .brand-name {
    font-size: 34px;
    line-height: 1.2;
    font-weight: 400;
    letter-spacing: 1px;
  }
  .contact-block {
    position: absolute;
    left: 520px;
    top: 78px;
    width: 440px;
    text-align: center;
  }
  .person-name {
    font-size: 46px;
    font-weight: 400;
    letter-spacing: 0.5px;
    line-height: 1.1;
  }
  .person-title {
    font-size: 30px;
    line-height: 1.2;
    margin-top: 4px;
  }
  .contact-list {
    list-style: none;
    margin-top: 90px;
    font-size: 26px;
    line-height: 38.5px;
  }
  .contact-label { font-weight: 700; }
  .address { margin-top: 4px; line-height: 35px; }
</style>
</head>
<body>
  <main class="canvas">
    <section class="business-card">
      <svg class="accent-arc" viewBox="0 0 1000 572" aria-hidden="true">
        <circle cx="163" cy="286" r="349" fill="none" stroke="var(--brand-blue)" stroke-width="30"/>
      </svg>

      <div class="brand-lockup">
        <div class="brand-mark"></div>
        <p class="brand-name">LearnWave<br>Progress Alliance</p>
      </div>

      <div class="contact-block">
        <h1 class="person-name">MARK HALVORSEN</h1>
        <p class="person-title">Founder</p>
        <ul class="contact-list">
          <li><span class="contact-label">O</span> (626) 555-0172</li>
          <li><span class="contact-label">F</span> (626) 555-0189</li>
          <li>learnwaveprogress.org</li>
          <li>mark@learnwaveprogress.org</li>
          <li class="address">412 West Marlow Ave, 6th Floor<br>Pasadena, CA 91187</li>
        </ul>
      </div>
    </section>
  </main>
</body>
</html>
```